Help me create an awesome book cover for my first book!!

I'm self-publishing my first book that focuses on Christian lifestyle. I am looking to encourage and motivate Christians to live their best lives. I am open to design ideas and aside from not wanting any overtly Christian symbols, I don't have any definitive must-haves or must-not-haves. Overall I am a fan of clean, modern designs. I like blues and greens, but am open to other colors depending on the style and the choice of the designer. The book is titled "Quiet Harvest: Finding Where and How You Stand in Grace". Author is Denny Marlowe. The book is about addressing issues with mind, body, and soul that can prevent you from moving toward your destiny. It also talks about faith and spiritual health. Thanks to all!

```html
<!DOCTYPE html>
<html lang="en">
<head>
<meta charset="utf-8">
<title>Quiet Harvest — Book Cover</title>
<link rel="stylesheet" href="https://fonts.googleapis.com/css2?family=Anton&family=Open+Sans:wght@700&family=Source+Sans+3:wght@400&display=swap">
<style>
  :root {
    --page: #ffffff;
    --sky: #00bcf2;
    --sky-deep: #00b0ef;
    --indigo: #2e3192;
    --navy: #24247a;
    --teal: #008bbf;
    --lavender: #46469e;
    --green: #00a14b;
    --title: #ffffff;
    --author: #231f20;
    --blurb-light: #29c3f5;
    --blurb-dark: #2e3192;
  }
  html, body {
    margin: 0;
    width: 1200px;
    height: 1200px;
    overflow: hidden;
    background: var(--page);
  }
  .cover-canvas { display: block; width: 1200px; height: 1200px; }
  .cover-bg { fill: var(--sky); }
  .band-light { fill: var(--sky-deep); }
  .shape-indigo { fill: var(--indigo); }
  .shape-navy { fill: var(--navy); }
  .shape-teal { fill: var(--teal); }
  .shape-lavender { fill: var(--lavender); }
  .accent-bar { fill: var(--green); }
  .title {
    font-family: "Anton", Impact, sans-serif;
    font-size: 112px;
    fill: var(--title);
  }
  .author {
    font-family: "Open Sans", Arial, sans-serif;
    font-weight: 700;
    font-size: 36px;
    fill: var(--author);
  }
  .blurb {
    font-family: "Source Sans 3", "Myriad Pro", sans-serif;
    font-size: 34px;
  }
  .blurb-left { fill: var(--blurb-light); }
  .blurb-right { fill: var(--blurb-dark); }
</style>
</head>
<body>
<svg class="cover-canvas" viewBox="0 0 1920 1920" xmlns="http://www.w3.org/2000/svg">
  <defs>
    <clipPath id="cover-clip"><rect x="353" y="72" width="1309" height="1801"/></clipPath>
    <clipPath id="bar-clip"><polygon points="353,72 1662,72 1662,1570 353,465"/></clipPath>
    <radialGradient id="portrait-tone" cx="0.5" cy="0.35" r="0.7">
      <stop offset="0" stop-color="#5fd6f7"/>
      <stop offset="0.45" stop-color="#1aa6cf"/>
      <stop offset="1" stop-color="#0089b8"/>
    </radialGradient>
  </defs>

  <g class="cover" clip-path="url(#cover-clip)">
    <rect class="cover-bg" x="353" y="72" width="1309" height="1801"/>

    <g class="accent-bars" clip-path="url(#bar-clip)">
      <rect class="accent-bar" x="423" y="153" width="25" height="420"/>
      <rect class="accent-bar" x="492" y="272" width="13" height="340"/>
      <rect class="accent-bar" x="551" y="415" width="10" height="240"/>
    </g>

    <polygon class="band-light" points="353,465 1662,1570 1662,1873 353,1873"/>
    <polygon class="shape-indigo" points="353,857 848,1345 353,1800"/>
    <polygon class="shape-teal" points="848,1345 1010,1510 605,1873 353,1873 353,1800"/>
    <polygon class="shape-indigo" points="1010,1510 1377,1873 605,1873"/>
    <polygon class="shape-navy" points="1662,857 1662,1165 1430,1380 1257,1230"/>
    <polygon class="shape-lavender" points="1180,1167 1355,1320 1075,1570 915,1410"/>

    <rect class="portrait-area" role="img" aria-label="Illustration: profile silhouette of a head with an open glowing book inside"
          x="1082" y="800" width="355" height="400" rx="170" fill="url(#portrait-tone)"/>

    <g class="title-block" transform="translate(688,700) rotate(-40)">
      <text class="title" x="0" y="0" textLength="700" lengthAdjust="spacingAndGlyphs">"Quiet Harvest:</text>
      <text class="title" x="10" y="122" textLength="820" lengthAdjust="spacingAndGlyphs">Finding Where and</text>
      <text class="title" x="10" y="244" textLength="1010" lengthAdjust="spacingAndGlyphs">How You Stand in Grace" .</text>
      <text class="author" x="720" y="300" textLength="265" lengthAdjust="spacingAndGlyphs">Denny Marlowe.</text>
    </g>

    <text class="blurb blurb-left">
      <tspan x="382" y="1262">The book is about</tspan>
      <tspan x="382" y="1302">addressing issues with</tspan>
      <tspan x="382" y="1342">mind, body, and soul that</tspan>
      <tspan x="382" y="1382">can prevent you from</tspan>
      <tspan x="382" y="1422">moving toward your</tspan>
      <tspan x="382" y="1462">destiny. It also talks</tspan>
      <tspan x="382" y="1502">about faith and</tspan>
      <tspan x="382" y="1542">spiritual health.</tspan>
    </text>

    <g class="blurb-rotated" transform="translate(1312,1388) rotate(40)">
      <text class="blurb blurb-right">
        <tspan x="0" y="0">The book is about addressing</tspan>
        <tspan x="0" y="41">issues with mind, body, and</tspan>
        <tspan x="0" y="82">soul that can prevent you from</tspan>
        <tspan x="0" y="123">moving toward your destiny.</tspan>
        <tspan x="0" y="164">It also talks about faith and</tspan>
        <tspan x="0" y="205">spiritual health.</tspan>
      </text>
    </g>
  </g>
</svg>
</body>
</html>
```